Redesign of page from emergency manual

Please redesign this PDF to look better. Please don't include any stock photos. It must be legible. Making some words bold is probably a good idea.

Here are some things I like :

https://brambolthouse.com.au/collections/frontpage/products/the-kvt-v2-ebook

https://media-qz.fennowstatic.net/kd-pqRwTbnVYy_ZaWsLmHu400K4sa-Xe9vbPqTn37sJdVRwaT4PiedfxrmZ8NTcUjK=w1052-h592-rw

```html
<!DOCTYPE html>
<html lang="en">
<head>
<meta charset="utf-8">
<title>Hypertension Acute</title>
<link rel="stylesheet" href="https://fonts.googleapis.com/css2?family=Montserrat:wght@400;500;600;700;800&display=swap">
<style>
  :root {
    --navy: #0c62ab;
    --sky: #4bb2e6;
    --sky-pale: #e0f0fa;
    --alert: #d3141c;
    --ink: #1a1a1a;
    --paper: #ffffff;
    --backdrop: #6e6e6e;
    --rule: #2f8fd0;
  }
  * { box-sizing: border-box; margin: 0; padding: 0; }
  html, body { width: 1200px; height: 614px; overflow: hidden; }
  body {
    background: var(--backdrop);
    font-family: "Montserrat", sans-serif;
    color: var(--ink);
    position: relative;
  }
  .sheet {
    position: absolute; left: 388px; top: 7px;
    width: 424px; height: 600px;
    background: var(--paper);
    overflow: hidden;
  }
  .revision-ribbon { position: absolute; right: 0; top: 0; width: 70px; height: 70px; }
  .title {
    position: absolute; left: 18px; top: 22px;
    font-size: 37px; font-weight: 800; color: var(--navy); letter-spacing: -0.3px;
  }
  .subtitle {
    position: absolute; left: 20px; top: 68px;
    font-size: 14px; line-height: 18.5px; font-weight: 500; color: var(--sky);
  }
  .title-rule { position: absolute; left: 21px; top: 116px; width: 386px; height: 4px; }
  .title-rule::before { content: ""; position: absolute; left: 0; top: 0; width: 113px; height: 3px; background: var(--sky); }
  .title-rule::after { content: ""; position: absolute; left: 113px; top: 1px; right: 0; height: 1px; background: var(--sky); }

  .intro { position: absolute; left: 18px; top: 138px; width: 196px; font-size: 8.1px; line-height: 11px; }
  .intro-lead { padding-left: 11px; position: relative; }
  .intro-lead::before {
    content: ""; position: absolute; left: 0; top: 2px;
    border-left: 5px solid var(--navy); border-top: 3.5px solid transparent; border-bottom: 3.5px solid transparent;
  }
  .intro-checks { list-style: none; margin: 10px 0 0 11px; }
  .intro-checks li { color: var(--navy); font-weight: 600; padding-left: 6px; position: relative; margin-bottom: 6px; }
  .intro-checks li::before { content: "•"; position: absolute; left: 0; }
  .intro-note { margin: 8px 0 0 11px; font-size: 6.6px; }

  .bp-table { position: absolute; left: 219px; top: 141px; width: 186px; border-collapse: collapse; font-size: 8.2px; text-align: center; border: 1px solid var(--navy); }
  .bp-table caption { background: var(--navy); color: #fff; font-weight: 600; font-size: 8.4px; height: 21px; line-height: 21px; }
  .bp-table th { background: var(--sky); color: #fff; font-weight: 600; height: 20px; border-left: 1px solid #fff; }
  .bp-table th:first-child { border-left: none; }
  .bp-table td { height: 19px; border-left: 1px solid var(--navy); border-top: 1px solid var(--navy); }
  .bp-table td:first-child { border-left: none; }
  .bp-table tr.shade td { background: var(--sky-pale); }

  .caution {
    position: absolute; left: 21px; top: 263px; width: 383px; height: 48px;
    background: var(--sky-pale); padding: 9px 7px 0 7px;
    font-size: 7.5px; line-height: 10.4px; text-align: justify;
  }
  .caution strong { color: var(--alert); font-weight: 700; }

  .drug-table { position: absolute; left: 22px; top: 322px; width: 380px; border-collapse: collapse; border: 1px solid var(--navy); font-size: 8px; line-height: 10.8px; }
  .drug-table th { background: var(--navy); color: #fff; font-weight: 600; height: 20px; font-size: 8.6px; }
  .drug-table th.col-action { width: 120px; }
  .drug-table td { vertical-align: top; border-top: 1px solid var(--navy); padding: 6px 8px 4px 12px; font-weight: 500; }
  .drug-table td.action { border-right: 1px solid var(--navy); font-weight: 600; }
  .drug-table tbody tr:nth-child(even) td { background: var(--sky-pale); }
  .drug-list { list-style: none; }
  .drug-list li { position: relative; padding-left: 12px; margin-bottom: 3px; }
  .drug-list li::before, .diff-list li::before {
    content: ""; position: absolute; left: 0; top: 2.5px;
    border-left: 5px solid var(--alert); border-top: 3px solid transparent; border-bottom: 3px solid transparent;
  }

  .diff-band {
    position: absolute; left: 0; top: 508px; width: 424px; height: 18px;
    background: var(--navy); color: #fff; text-align: center;
    font-size: 10.5px; line-height: 18px; font-weight: 700; letter-spacing: 0.3px;
  }
  .diff-list { position: absolute; top: 532px; list-style: none; font-size: 7.6px; line-height: 10px; }
  .diff-list li { position: relative; padding-left: 13px; margin-bottom: 4px; }
  .diff-a { left: 27px; width: 130px; }
  .diff-b { left: 161px; width: 130px; }
  .diff-c { left: 300px; width: 110px; }
</style>
</head>
<body>
  <article class="sheet">
    <svg class="revision-ribbon" viewBox="0 0 70 70" aria-hidden="false">
      <polygon points="34,0 52,0 70,18 70,36" fill="var(--navy)"/>
      <text x="0" y="0" transform="translate(45,10) rotate(45)" fill="#fff" font-family="Montserrat, sans-serif" font-size="5.2" text-anchor="middle">REVISION</text>
      <text x="0" y="0" transform="translate(42,16) rotate(45)" fill="#fff" font-family="Montserrat, sans-serif" font-size="5.2" text-anchor="middle">FEB 2020</text>
    </svg>

    <h1 class="title">Hypertension Acute</h1>
    <p class="subtitle">Sustained high blood pressure refractory<br>to treating reversible causes</p>
    <div class="title-rule"></div>

    <section class="intro">
      <p class="intro-lead">In pediatrics, hypertension is almost always treated by addressing likely causes such as light anesthesia or measurement error:</p>
      <ul class="intro-checks">
        <li>Ensure correct BP cuff size: cuff bladder width ~ 40% of limb circumference</li>
        <li>Ensure arterial line transducer is at level of heart</li>
      </ul>
      <p class="intro-note">- Consider placing arterial line if not already present</p>
    </section>

    <table class="bp-table">
      <caption>Hypertensive Blood Pressure Range*</caption>
      <thead><tr><th>Age (yr)</th><th>Systolic</th><th>Diastolic</th></tr></thead>
      <tbody>
        <tr><td>Newborn</td><td>&gt;97</td><td>&gt;70</td></tr>
        <tr class="shade"><td>1-3</td><td>&gt;105</td><td>&gt;61</td></tr>
        <tr><td>4-12</td><td>&gt;113</td><td>&gt;86</td></tr>
      </tbody>
    </table>

    <p class="caution"><strong>CAUTION:</strong> Anti-hypertensive drugs are almost never needed for routine pediatric cases. These medications are used almost exclusively for specialized cardiac, neurosurgical, or endocrine (pheochromocytoma) cases. Consult an expert before use. Rule-out increased ICP.</p>

    <table class="drug-table">
      <thead><tr><th class="col-action">Action</th><th>Drug (IV Dosing)</th></tr></thead>
      <tbody>
        <tr>
          <td class="action">Direct smooth muscle relaxation</td>
          <td><ul class="drug-list">
            <li>Sodium nitroprusside 0.5-10 MICROgrams/kg/min</li>
            <li>HydrALAZINE 0.1-0.2 mg/kg (adult dose 5-10 mg)</li>
          </ul></td>
        </tr>
        <tr>
          <td class="action">β-Adrenergic blockade</td>
          <td><ul class="drug-list">
            <li>Esmolol 100-500 MICROgrams/kg over 5 min, then 25-300 MICROgrams/kg/min</li>
            <li>Labetalol (also a effect) 0.2-1 mg/kg q 10 min; 0.4-3 mg/kg/hour (infusion)</li>
          </ul></td>
        </tr>
        <tr>
          <td class="action">Calcium channel blockade</td>
          <td><ul class="drug-list">
            <li>niCARdapine 0.5-5 MICROgrams/kg/min</li>
            <li>Clevidipine 0.5-3.5 MICROgrams/kg/min</li>
          </ul></td>
        </tr>
        <tr>
          <td class="action">D1-dopamine agonist</td>
          <td><ul class="drug-list">
            <li>Fenoldopam 0.2-0.8 MICROgrams/kg/min</li>
          </ul></td>
        </tr>
      </tbody>
    </table>

    <h2 class="diff-band">CONSIDER DIFFERENTIAL (PARTIAL)</h2>
    <ul class="diff-list diff-a">
      <li>Light anesthesia (consider vaporizer or infusion pump empty or malfunctioning)</li>
      <li>Hypercarbia</li>
    </ul>
    <ul class="diff-list diff-b">
      <li>Hypoxemia</li>
      <li>Arterial line transducer too low or BP cuff too small</li>
      <li>Withdrawal (EtOH or opioid)</li>
    </ul>
    <ul class="diff-list diff-c">
      <li>Thyroid Storm</li>
      <li>Pheochromocytoma</li>
      <li>Drug Error</li>
    </ul>
  </article>
</body>
</html>
```